Multi-purose Thank You Card Design Project (Real Estate)

We are in the business of listing and selling luxury homes in Atlanta Georgia and are the #1 Award Winning team in our office, #5 in Georgia and #5 in Southeast for all Brandt Halloway team. Your can learn more about us at www.marrowbyandpartners.example.

In our business model, growing a team to $80 million in sales (we will sell $40,000,000 in 2013 and are determined to grow rapidly while providing high levels of service) requires that we carefully nurture our sphere of influence database through multiple, high quality, well-designed touches like (thank you cards, letters, phone calls, gifts etc)

We need a thank you card:
1. Can be used for multiple purposes
a. Referral thank you.
b. House closing anniversary thank you
2. File built in Photoshop with layers that we can edit (we are proficient in Photoshop)
3. Design based on the Brandt Halloway luxury Style Guide but does not restrict your creativity. Break the rules and have more impact.
5. Card 7" w x 5' h opening at top
Updates

The first place payment guarantee has been increased by $100 to $320.

The attached logo files have been replaced and should open correctly.
Kindly,
Pelford

Target Market(s)

Buyers and Seller of Homes from $300k to $10m

Industry/Entity Type

Business

Requirements
Must have
• Copy on cover: "Thanks for the Referral"
Logo 1: Brandt Halloway Luxury Logo
File in 300 dpi for print
File in 96 dpi for use with Post Ahead Notes
Nice to have
• Photo of Home (optional)
Logo 2 Marrowby and Partners Logo (optional)

```html
<!DOCTYPE html>
<html lang="en">
<head>
<meta charset="utf-8">
<title>Thanx for the Referral – Card Cover</title>
<link href="https://fonts.googleapis.com/css2?family=Pinyon+Script&family=Open+Sans:wght@400&display=swap" rel="stylesheet">
<style>
  :root {
    --backdrop: #000000;
    --card: #eef2db;
    --card-edge: #d9dcc6;
    --script: #a9a79c;
    --script-shadow: #4a4a40;
    --caption: #3d3d36;
    --photo-leaf: #4f7a2c;
    --photo-stone: #9c8f74;
  }
  html, body {
    margin: 0;
    padding: 0;
    width: 1200px;
    height: 900px;
    overflow: hidden;
    background: var(--backdrop);
  }
  .canvas {
    position: relative;
    width: 1200px;
    height: 900px;
    background: var(--backdrop);
  }
  .card-cover {
    position: absolute;
    left: 180px;
    top: 151px;
    width: 838px;
    height: 597px;
    background: var(--card);
    box-shadow: inset 0 0 0 1px var(--card-edge);
  }
  .home-photo {
    position: absolute;
    left: 191px;
    top: 225px;
    width: 457px;
    height: 102px;
    background: linear-gradient(90deg, var(--photo-leaf) 0%, var(--photo-stone) 45%, var(--photo-leaf) 100%);
  }
  .headline {
    position: absolute;
    left: 378px;
    top: 276px;
    margin: 0;
    font-family: "Pinyon Script", cursive;
    font-weight: 400;
    font-size: 124px;
    line-height: 1;
    color: var(--script);
    text-shadow: 1px 1px 0 var(--script-shadow), 2px 2px 2px rgba(0,0,0,0.35);
    letter-spacing: -2px;
  }
  .subline {
    position: absolute;
    left: 501px;
    top: 372px;
    margin: 0;
    font-family: "Open Sans", sans-serif;
    font-size: 11px;
    line-height: 1;
    letter-spacing: 1.6px;
    color: var(--caption);
  }
</style>
</head>
<body>
  <div class="canvas">
    <section class="card-cover">
      <div class="home-photo" role="img" aria-label="Photograph of a stone luxury home with gabled roofs framed by green trees and hedges"></div>
      <h1 class="headline">Thanx</h1>
      <p class="subline">for the Referral</p>
    </section>
  </div>
</body>
</html>
```